Wordpress website update with basic ecomm features

We need an update to our existing website
www.brightmoorhub.com.au that can be easily updated, enhances our logo and can take payments online and a basic text logo suite for 3 products. Website would reflect confidence and give clients confidence in the outcomes we will provide for them. must be easy to use, crisp, fresh, clean and dynamic.

Target Market(s)

entrepreneurs, professionals, small business owners, corporate organisations, universities

Industry/Entity Type

Online

Coding

Coded - Design and coding required

Number of Pages Required

5+ page

Font styles to use
Sans Serif

Requirements
Must have
• be easy to navigate, look professional, please see brief doc
Nice to have
• please see briefing doc
Should not have
• please see briefing doc

```html
<!DOCTYPE html>
<html lang="en">
<head>
<meta charset="utf-8">
<title>Brightmoor Hub</title>
<link href="https://fonts.googleapis.com/css2?family=Cinzel:wght@400;700&family=Open+Sans:wght@400;600;700&display=swap" rel="stylesheet">
<style>
:root{
  --ink:#1d1d1f;
  --text:#555;
  --muted:#888;
  --line:#d9d9d9;
  --paper:#fff;
  --mist:#eeeeee;
  --dark:#151515;
  --accent:#2b2b2b;
  --social-a:#3b5b9a;
  --social-b:#2aa3d6;
  --social-c:#c7362b;
}
*{box-sizing:border-box;margin:0;padding:0}
html,body{width:1200px;height:4044px;overflow:hidden}
body{font-family:"Open Sans",Arial,sans-serif;color:var(--text);background:var(--paper);font-size:13px;line-height:1.6;position:relative}
.serif{font-family:"Cinzel",Georgia,serif}
section,header,footer{position:absolute;left:0;width:1200px;overflow:hidden}
.wordmark{display:flex;align-items:center;gap:12px}
.wordmark .mark{width:52px;height:52px;background:var(--ink)}
.wordmark .name{font-family:"Cinzel",Georgia,serif;font-weight:700;font-size:22px;color:var(--ink);letter-spacing:2px;text-transform:uppercase}
.social{display:flex;gap:8px}
.social span{width:22px;height:22px;border-radius:50%;display:block}
.social span:nth-child(1){background:var(--social-a)}
.social span:nth-child(2){background:var(--social-b)}
.social span:nth-child(3){background:var(--social-a)}
.social span:nth-child(4){background:var(--social-c)}

/* header */
.site-header{top:0;height:160px}
.site-header .wordmark{position:absolute;left:80px;top:34px}
.top-contact{position:absolute;right:80px;top:14px;display:flex;flex-direction:column;align-items:flex-end;gap:10px;font-size:12px;color:var(--ink)}
.top-contact .lines{display:flex;gap:26px}
.main-nav{position:absolute;left:370px;top:116px;display:flex;gap:30px;font-size:13px;font-weight:600;color:var(--ink)}
.main-nav a{color:inherit;text-decoration:none;padding-bottom:6px}
.main-nav a.active{border-bottom:2px solid var(--ink)}

/* hero */
.hero{top:160px;height:480px}
.hero-photo{position:absolute;inset:0;background:linear-gradient(180deg,#c9cfd4 0%,#8f9498 45%,#4a4540 100%)}
.hero-arrow{position:absolute;top:200px;width:30px;height:40px;background:rgba(0,0,0,.7)}
.hero-arrow svg{display:block;margin:12px auto}
.hero-band{position:absolute;left:0;right:0;bottom:0;height:96px;background:linear-gradient(180deg,rgba(0,0,0,.2),rgba(0,0,0,.8));display:flex;align-items:center;justify-content:center;text-align:center}
.hero-band p{font-family:"Cinzel",Georgia,serif;font-weight:700;color:#fff;font-size:24px;line-height:1.3;letter-spacing:.5px}

/* welcome */
.welcome{top:640px;height:480px}
.section-title{font-family:"Cinzel",Georgia,serif;font-weight:700;color:var(--ink);font-size:36px;text-align:center;letter-spacing:1px}
.lede{text-align:center;font-weight:700;color:var(--ink);font-size:14px;width:1000px;margin:8px auto 0;line-height:1.5}
.welcome .section-title{margin-top:44px}
.tabs{position:absolute;left:80px;top:200px;width:340px;list-style:none;text-align:right}
.tabs li{font-family:"Cinzel",Georgia,serif;font-size:15px;color:var(--muted);padding:11px 16px;border-bottom:1px solid transparent;margin-bottom:12px}
.tabs li.active{color:var(--ink);border:1px solid var(--line);border-right:none;background:#fafafa}
.tab-body{position:absolute;left:450px;top:200px;width:670px;border-left:1px solid var(--line);padding-left:22px;font-size:12px}
.tab-body p{margin-bottom:14px}
.ticks{list-style:none}
.ticks li{display:flex;gap:10px;align-items:center;margin-bottom:8px}
.ticks svg{flex:none}

/* offering */
.offering{top:1140px;height:560px;background:linear-gradient(180deg,#f4f4f4,#e2e2e2)}
.offering .section-title{margin-top:50px}
.offering .lede{font-size:13px}
.ring{position:absolute;left:360px;top:240px;width:480px;height:480px;border-radius:50%;border:2px solid #fff;box-shadow:0 0 0 1px #cfcfcf}
.node{position:absolute;display:flex;flex-direction:column;align-items:center;gap:10px;font-family:"Cinzel",Georgia,serif;font-weight:700;color:var(--ink);font-size:17px;text-align:center;line-height:1.2}
.node .icon{width:58px;height:58px;border-radius:50%;background:var(--ink);display:flex;align-items:center;justify-content:center}
.node.top{left:520px;top:188px}
.node.side{flex-direction:row;gap:14px}
.node.left{left:180px;top:366px}
.node.right{left:790px;top:366px}
.centre-mark{position:absolute;left:490px;top:420px;width:220px;height:110px;background:#fff;border:1px solid var(--line);display:flex;align-items:center;justify-content:center}
.centre-mark .mark{width:40px;height:40px}
.centre-mark .name{font-size:15px}

/* value */
.value{top:1712px;height:470px;background:var(--dark)}
.value-photo{position:absolute;left:0;top:0;width:560px;height:470px;background:linear-gradient(120deg,#d8cbb8 0%,#a89580 50%,#514840 100%)}
.value-panel{position:absolute;left:560px;top:0;width:640px;height:470px;padding:34px 40px;background:linear-gradient(90deg,rgba(21,21,21,.6),var(--dark) 30%)}
.value-panel h2{font-family:"Cinzel",Georgia,serif;color:#fff;font-size:32px;font-weight:700;margin-bottom:16px}
.value-panel .ticks li{color:#ddd;font-size:12px;margin-bottom:6px}

/* events */
.events{top:2192px;height:580px}
.title-rule{display:flex;align-items:center;justify-content:center;gap:24px;margin-top:40px}
.title-rule::before,.title-rule::after{content:"";height:1px;width:250px;background:var(--line)}
.title-rule h2{font-family:"Cinzel",Georgia,serif;color:var(--ink);font-size:34px;font-weight:700}
.cards{position:absolute;top:140px;left:80px;display:flex;gap:25px}
.card{width:330px;height:370px;border:1px solid var(--line);background:#fff;box-shadow:0 2px 6px rgba(0,0,0,.08)}
.card .pic{height:190px;margin:8px;background:linear-gradient(160deg,#e8eaec,#9aa3ab)}
.card .meta{display:flex;gap:12px;padding:10px 16px}
.card .date{width:44px;text-align:center;flex:none}
.card .date b{display:block;background:var(--ink);color:#fff;font-size:14px;line-height:26px}
.card .date span{display:block;font-size:10px;color:var(--muted);border:1px solid var(--line);border-top:none}
.card p{font-size:11px;line-height:1.6}
.pager{position:absolute;top:528px;left:0;right:0;display:flex;justify-content:center;gap:8px}
.pager i{width:8px;height:8px;border-radius:50%;background:#ccc}
.pager i:first-child{background:var(--ink)}

/* faq + testimonials */
.faq-testi{top:2772px;height:470px}
.col-title{font-family:"Cinzel",Georgia,serif;color:var(--ink);font-size:32px;font-weight:700;border-bottom:1px solid var(--ink);padding-bottom:6px}
.faq{position:absolute;left:80px;top:40px;width:510px}
.faq ul{list-style:none;margin-top:18px}
.faq li{display:flex;justify-content:space-between;align-items:center;background:#f1f1f1;border:1px solid #e2e2e2;padding:0 14px;height:48px;margin-bottom:8px;font-size:12px;color:var(--ink)}
.faq li:first-child{background:var(--ink);color:#fff}
.faq li .q{display:flex;gap:10px;align-items:center}
.faq li .q b{font-size:16px}
.faq li .d{font-size:11px;color:var(--muted)}
.faq li:first-child .d{color:#bbb}
.testi{position:absolute;left:640px;top:40px;width:480px}
.testi .body{display:flex;gap:20px;margin-top:24px}
.avatar{width:96px;height:96px;border-radius:50%;background:linear-gradient(160deg,#e2cbb2,#9c8068);flex:none;border:3px solid #eee}
.testi blockquote{font-size:13px;line-height:1.8;position:relative}
.testi blockquote::before{content:"\201C";font-family:"Cinzel",Georgia,serif;font-size:48px;color:#ccc;position:absolute;left:-4px;top:-30px}
.testi cite{display:block;text-align:right;font-family:"Cinzel",Georgia,serif;font-style:normal;color:var(--ink);margin-top:14px;font-size:14px}

/* callback */
.callback{top:3242px;height:318px;background:#f2f2f2}
.callback .section-title{margin-top:30px;font-size:32px}
.form{position:absolute;left:80px;top:110px;width:1040px;display:grid;grid-template-columns:repeat(3,1fr);gap:14px 20px}
.field{height:38px;background:#fff;border:1px solid #d4d4d4;font-size:11px;color:var(--muted);padding:0 12px;display:flex;align-items:center;justify-content:space-between}
.submit{position:absolute;left:520px;top:266px;width:160px;height:38px;background:var(--ink);color:#fff;font-family:"Cinzel",Georgia,serif;font-weight:700;letter-spacing:2px;display:flex;align-items:center;justify-content:center;font-size:14px}

/* footer */
.site-footer{top:3560px;height:484px;background:linear-gradient(180deg,#1b1c24 0%,#2a2420 55%,#0e0e10 100%);color:#ddd}
.contact-row{position:absolute;top:54px;left:0;right:0;display:flex;justify-content:space-around;padding:0 140px;font-size:12px}
.contact-row div{display:flex;flex-direction:column;align-items:center;gap:10px}
.site-footer .wordmark{position:absolute;left:0;right:0;top:176px;justify-content:center}
.site-footer .wordmark .mark{background:#fff;width:44px;height:44px}
.site-footer .wordmark .name{color:#fff}
.foot-nav{position:absolute;top:290px;left:0;right:0;display:flex;justify-content:center;gap:28px;font-size:13px;font-weight:600;color:#fff}
.bottom-bar{position:absolute;left:0;right:0;bottom:0;height:64px;background:rgba(0,0,0,.6);display:flex;align-items:center;justify-content:space-between;padding:0 80px;font-size:11px}
</style>
</head>
<body>

<header class="site-header">
  <div class="wordmark"><span class="mark"></span><span class="name">Brightmoor Hub</span></div>
  <div class="top-contact">
    <div class="social"><span></span><span></span><span></span><span></span></div>
    <div class="lines"><span>(123) 456-7890</span><span>info@brightmoorhub.com.au</span></div>
  </div>
  <nav class="main-nav">
    <a class="active">Home</a><a>Who Brightmoor Hub</a><a>About</a><a>FAQs</a><a>Testimonials</a><a>Upcoming Events</a><a>Contact</a>
  </nav>
</header>

<section class="hero">
  <div class="hero-photo" role="img" aria-label="Team of professionals working together around a table in a bright office"></div>
  <div class="hero-arrow" style="left:0"><svg width="8" height="14" viewBox="0 0 8 14"><path d="M7 1 1 7l6 6" stroke="#fff" stroke-width="2" fill="none"/></svg></div>
  <div class="hero-arrow" style="right:0"><svg width="8" height="14" viewBox="0 0 8 14"><path d="m1 1 6 6-6 6" stroke="#fff" stroke-width="2" fill="none"/></svg></div>
  <div class="hero-band"><p>Builds and develops validation and innovation programs,<br>communities and data to improve the overall success</p></div>
</section>

<section class="welcome">
  <h1 class="section-title">Welcome To Brightmoor Hub</h1>
  <p class="lede">We help founders, teams and organisations test ideas, grow strong networks and use clear data to reach real results. Our programs turn plans into steady progress you can measure.</p>
  <ul class="tabs">
    <li class="active">Outline of Program</li>
    <li>What we deliver</li>
    <li>Outcomes</li>
    <li>What comes with the program</li>
    <li>How the modules are structured?</li>
  </ul>
  <div class="tab-body">
    <p>Each program starts with a short review of your goals, your market and your team. From there we build a clear plan with weekly steps, simple checkpoints and honest feedback, so every stage moves you closer to a result you can show to clients and investors.</p>
    <ul class="ticks">
      <li><svg width="12" height="12" viewBox="0 0 12 12"><path d="m1 6 3 3 7-7" stroke="#1d1d1f" stroke-width="2" fill="none"/></svg>Guided sessions with experienced mentors each week</li>
      <li><svg width="12" height="12" viewBox="0 0 12 12"><path d="m1 6 3 3 7-7" stroke="#1d1d1f" stroke-width="2" fill="none"/></svg>Practical tools to test demand before you build</li>
      <li><svg width="12" height="12" viewBox="0 0 12 12"><path d="m1 6 3 3 7-7" stroke="#1d1d1f" stroke-width="2" fill="none"/></svg>Access to a network of peers and partners</li>
      <li><svg width="12" height="12" viewBox="0 0 12 12"><path d="m1 6 3 3 7-7" stroke="#1d1d1f" stroke-width="2" fill="none"/></svg>Clear reports that track progress against goals</li>
      <li><svg width="12" height="12" viewBox="0 0 12 12"><path d="m1 6 3 3 7-7" stroke="#1d1d1f" stroke-width="2" fill="none"/></svg>Workshops on pricing, sales and growth planning</li>
      <li><svg width="12" height="12" viewBox="0 0 12 12"><path d="m1 6 3 3 7-7" stroke="#1d1d1f" stroke-width="2" fill="none"/></svg>Ongoing support after the program ends</li>
    </ul>
  </div>
</section>

<section class="offering">
  <h2 class="section-title">About Our Offering</h2>
  <p class="lede">Three connected parts that give every participant a clear path from first idea to lasting results.</p>
  <div class="ring"></div>
  <div class="node top"><span>What we<br>deliver</span><span class="icon"><svg width="24" height="26" viewBox="0 0 24 26"><rect x="3" y="4" width="18" height="20" rx="2" fill="none" stroke="#fff" stroke-width="2"/><rect x="8" y="1" width="8" height="5" fill="#fff"/><path d="M7 12h10M7 17h10" stroke="#fff" stroke-width="2"/></svg></span></div>
  <div class="node side left"><span>Outline of<br>program</span><span class="icon"><svg width="24" height="20" viewBox="0 0 24 20"><rect x="2" y="5" width="20" height="13" rx="2" fill="none" stroke="#fff" stroke-width="2"/><path d="M8 5V2h8v3" stroke="#fff" stroke-width="2" fill="none"/></svg></span></div>
  <div class="node side right"><span class="icon"><svg width="24" height="24" viewBox="0 0 24 24"><circle cx="12" cy="12" r="9" fill="none" stroke="#fff" stroke-width="2"/><path d="M12 6v6l4 3" stroke="#fff" stroke-width="2" fill="none"/></svg></span><span>Our<br>Agenda</span></div>
  <div class="centre-mark wordmark"><span class="mark"></span><span class="name">Brightmoor Hub</span></div>
</section>

<section class="value">
  <div class="value-photo" role="img" aria-label="Smiling business team standing together"></div>
  <div class="value-panel">
    <h2>Our Value Proposition</h2>
    <ul class="ticks">
      <li><svg width="12" height="12" viewBox="0 0 12 12"><path d="m1 6 3 3 7-7" stroke="#fff" stroke-width="2" fill="none"/></svg>Real Business Education</li>
      <li><svg width="12" height="12" viewBox="0 0 12 12"><path d="m1 6 3 3 7-7" stroke="#fff" stroke-width="2" fill="none"/></svg>Expert Facilitators Who Have Built And Scaled Companies</li>
      <li><svg width="12" height="12" viewBox="0 0 12 12"><path d="m1 6 3 3 7-7" stroke="#fff" stroke-width="2" fill="none"/></svg>Live Collaboration In A Focused Setting, Every Week</li>
      <li><svg width="12" height="12" viewBox="0 0 12 12"><path d="m1 6 3 3 7-7" stroke="#fff" stroke-width="2" fill="none"/></svg>Tailored, Personal And Social Outcomes</li>
      <li><svg width="12" height="12" viewBox="0 0 12 12"><path d="m1 6 3 3 7-7" stroke="#fff" stroke-width="2" fill="none"/></svg>Sound Reasoning</li>
      <li><svg width="12" height="12" viewBox="0 0 12 12"><path d="m1 6 3 3 7-7" stroke="#fff" stroke-width="2" fill="none"/></svg>Powerful Networks</li>
      <li><svg width="12" height="12" viewBox="0 0 12 12"><path d="m1 6 3 3 7-7" stroke="#fff" stroke-width="2" fill="none"/></svg>Investment &amp; Industry Partnerships</li>
      <li><svg width="12" height="12" viewBox="0 0 12 12"><path d="m1 6 3 3 7-7" stroke="#fff" stroke-width="2" fill="none"/></svg>Informal And Formal Meet-ups</li>
      <li><svg width="12" height="12" viewBox="0 0 12 12"><path d="m1 6 3 3 7-7" stroke="#fff" stroke-width="2" fill="none"/></svg>Coaching To Ensure Focus And Continued Progress</li>
      <li><svg width="12" height="12" viewBox="0 0 12 12"><path d="m1 6 3 3 7-7" stroke="#fff" stroke-width="2" fill="none"/></svg>Community, Not Simply Network, Of Like-minded Individuals</li>
      <li><svg width="12" height="12" viewBox="0 0 12 12"><path d="m1 6 3 3 7-7" stroke="#fff" stroke-width="2" fill="none"/></svg>Validation And Lean Methods Applied To Your Work</li>
    </ul>
  </div>
</section>

<section class="events">
  <div class="title-rule"><h2>Upcoming Events</h2></div>
  <div class="cards">
    <article class="card"><div class="pic" role="img" aria-label="Hands working over papers at a meeting"></div><div class="meta"><div class="date"><b>24</b><span>Nov</span></div><p>Founders breakfast with short talks on testing new ideas, followed by open questions and time to meet other members.</p></div></article>
    <article class="card"><div class="pic" role="img" aria-label="Presenter speaking to a seated group"></div><div class="meta"><div class="date"><b>28</b><span>Nov</span></div><p>Half-day workshop on pricing and sales for small teams, with worked examples and a plan you can use straight away.</p></div></article>
    <article class="card"><div class="pic" role="img" aria-label="Speaker pointing at a board in a seminar"></div><div class="meta"><div class="date"><b>04</b><span>Dec</span></div><p>Evening panel on growth and funding, where local leaders share lessons from their own ventures and answer questions.</p></div></article>
  </div>
  <div class="pager"><i></i><i></i></div>
</section>

<section class="faq-testi">
  <div class="faq">
    <h2 class="col-title">FAQ's</h2>
    <ul>
      <li><span class="q"><b>−</b>Who is the program designed for?</span><span class="d">24 Nov 2016</span></li>
      <li><span class="q"><b>+</b>How long does each module run?</span><span class="d">24 Nov 2016</span></li>
      <li><span class="q"><b>+</b>Can I join part way through?</span><span class="d">24 Nov 2016</span></li>
      <li><span class="q"><b>+</b>Are sessions held online?</span><span class="d">24 Nov 2016</span></li>
      <li><span class="q"><b>+</b>What support comes afterwards?</span><span class="d">24 Nov 2016</span></li>
      <li><span class="q"><b>+</b>How do I pay for a place?</span><span class="d">24 Nov 2016</span></li>
    </ul>
  </div>
  <div class="testi">
    <h2 class="col-title">Client Testimonials</h2>
    <div class="body">
      <div class="avatar" role="img" aria-label="Portrait of a client"></div>
      <div>
        <blockquote>The program gave our team a clear plan and the confidence to act on it. Within weeks we had tested our idea, found our first customers and built a network we still rely on today.</blockquote>
        <cite>- Mrs. Clara Webb</cite>
      </div>
    </div>
  </div>
</section>

<section class="callback">
  <h2 class="section-title">Request A Call Back</h2>
  <div class="form">
    <div class="field">Name</div>
    <div class="field">Email</div>
    <div class="field">Phone number</div>
    <div class="field">Location, are you based in the city <span>▾</span></div>
    <div class="field">Do you have a current business <span>▾</span></div>
    <div class="field">Is your business in growth stage <span>▾</span></div>
    <div class="field">How many people are in the team <span>▾</span></div>
    <div class="field">How did you hear about us <span>▾</span></div>
    <div class="field">Business sector <span>▾</span></div>
  </div>
  <div class="submit">Submit</div>
</section>

<footer class="site-footer" role="img" aria-label="City skyline at night">
  <div class="contact-row">
    <div><svg width="18" height="24" viewBox="0 0 18 24"><path d="M9 23s8-9 8-14A8 8 0 0 0 1 9c0 5 8 14 8 14z" fill="none" stroke="#fff" stroke-width="2"/><circle cx="9" cy="9" r="3" fill="#fff"/></svg><span>14 Harbour Lane, Brightmoor</span></div>
    <div><svg width="22" height="22" viewBox="0 0 22 22"><path d="M5 2h4l2 5-3 2a12 12 0 0 0 5 5l2-3 5 2v4a2 2 0 0 1-2 2A18 18 0 0 1 3 4a2 2 0 0 1 2-2z" fill="#fff"/></svg><span>Phone: (123) 456-7890</span></div>
    <div><svg width="24" height="18" viewBox="0 0 24 18"><rect x="1" y="1" width="22" height="16" fill="none" stroke="#fff" stroke-width="2"/><path d="m1 1 11 9 11-9" fill="none" stroke="#fff" stroke-width="2"/></svg><span>Email: info@brightmoorhub.com.au</span></div>
  </div>
  <div class="wordmark"><span class="mark"></span><span class="name">Brightmoor Hub</span></div>
  <nav class="foot-nav"><span>Home</span><span>Who Brightmoor Hub</span><span>About</span><span>FAQs</span><span>Testimonials</span><span>Upcoming Events</span><span>Contact</span></nav>
  <div class="bottom-bar">
    <span>Copyright © 2016 Brightmoor Hub. All Rights Reserved.</span>
    <div class="social"><span></span><span></span><span></span><span></span></div>
  </div>
</footer>

</body>
</html>
```